Rovilent.com Trucking Company Website

Need a website designed (no content) for a trucking company, specializing in trucking of ocean containers (intermodal Trucking). Heavy emphasis on technology, using latest technology, providing unabated visibility and realtime information.
clean minimalist industrial website
example:
https://www.belquarn.com/

Target Market(s)

Professional Business Consumer corporate and small business

Industry/Entity Type

Trucking Company

Number of Pages Required

5+ page

Requirements
Must have
• Industrial Design, simple informative, for a busy professional to view and get the necessary information with out the distractions.
• Blog Page
• Client Log-In on the front page
• Technology page - showing our intensive investments in technology
Nice to have
• If ANY images included, MUST be USA related. Example if include an image of a truck, ensure its a USA model. Do the research.
• included our business card for sample of Logo
• Doesnt not have to be the same color schemes.
Should not have
• moving images

```html
<!DOCTYPE html>
<html lang="en">
<head>
<meta charset="utf-8">
<title>Rovilent.com — Logistics Services</title>
<link rel="stylesheet" href="https://fonts.googleapis.com/css2?family=Montserrat:wght@300;400;500;600;700&display=swap">
<style>
:root{
  --brand-blue:#15589a;
  --deep-blue:#0e3f7c;
  --ink:#111111;
  --grey-band:#eff0f2;
  --line:#dedfe2;
  --number-grey:#e9eaec;
  --partner-grey:#b5b6b8;
  --white:#ffffff;
}
*{box-sizing:border-box;margin:0;padding:0}
html,body{width:1133px;height:1200px;overflow:hidden;background:var(--white)}
body{font-family:'Montserrat',Arial,sans-serif;color:var(--ink);position:relative}
.canvas{position:relative;width:1133px;height:1200px;overflow:hidden}

.hero{position:absolute;left:0;top:0;width:1133px;height:506px}
.hero-visual{position:absolute;left:0;top:0}
.brand{position:absolute;left:40px;top:28px;display:flex;align-items:center;gap:8px}
.brand-mark{width:14px;height:14px;background:var(--brand-blue)}
.brand-name{font-size:26px;font-weight:700;color:var(--brand-blue);letter-spacing:.5px}
.hero-phone{position:absolute;right:36px;top:24px;display:flex;align-items:center;gap:10px;color:var(--white);font-size:15px;font-weight:400}
.client-login{position:absolute;right:36px;top:58px;height:28px;padding:0 14px;border:1px solid rgba(255,255,255,.85);color:var(--white);font-size:10px;font-weight:600;letter-spacing:.4px;display:flex;align-items:center;gap:7px;text-decoration:none}
.hero-copy{position:absolute;left:41px;top:206px;font-size:28px;font-weight:300;line-height:33px}
.hero-copy strong{font-weight:700}
.btn-outline{position:absolute;left:41px;top:355px;width:100px;height:34px;border:1px solid #cfcfcf;font-size:10px;display:flex;align-items:center;justify-content:center;color:var(--ink)}
.slider-dots{position:absolute;left:1101px;top:245px;display:flex;flex-direction:column;gap:3px}
.slider-dots span{width:4px;height:5px;background:var(--ink)}
.slider-dots span:first-child{background:var(--white)}

.section-bg{position:absolute;left:0;top:506px}
.main-nav{position:absolute;top:506px;left:0;width:1133px;height:68px;border-bottom:1px solid var(--line)}
.main-nav a{position:absolute;top:28px;font-size:10.5px;font-weight:600;color:var(--ink);text-decoration:none;letter-spacing:.2px}

.expertise-tag{position:absolute;left:334px;top:697px}
.expertise-title{position:absolute;left:381px;top:703px;font-size:35px;font-weight:700;color:var(--white)}
.expertise-list{position:absolute;left:686px;top:660px;width:258px;list-style:none}
.expertise-item{position:absolute;left:0;width:258px}
.expertise-num{position:absolute;left:0;font-size:38px;font-weight:600;color:var(--number-grey);line-height:38px}
.expertise-label{position:absolute;left:77px;font-size:14.4px;font-weight:700;line-height:18px;width:190px}
.expertise-rule{position:absolute;left:7px;width:251px;height:1px;background:var(--line)}

.quote-btn{position:absolute;left:606px;top:902px}
.quote-label{position:absolute;left:645px;top:922px;font-size:18px;font-weight:700;color:var(--white);display:flex;align-items:center;gap:14px}

.partners{position:absolute;left:0;top:1012px;width:1133px;height:108px;border-top:1px solid var(--line);border-bottom:1px solid var(--line)}
.partner{position:absolute;top:40px;background:var(--partner-grey);border-radius:4px}

.footer-left,.footer-right{position:absolute;top:1150px;font-size:9px;line-height:13px;color:var(--ink)}
.footer-left{left:21px}
.footer-right{left:1003px}
</style>
</head>
<body>
<div class="canvas">

  <header class="hero">
    <svg class="hero-visual" width="1133" height="506" viewBox="0 0 1133 506" role="img" aria-label="Two blue box trucks driving fast on a highway">
      <defs>
        <linearGradient id="skyGrad" x1="0" y1="0" x2="1" y2="1">
          <stop offset="0" stop-color="#a9bfd3"/>
          <stop offset=".6" stop-color="#c7d3de"/>
          <stop offset="1" stop-color="#9aa7b4"/>
        </linearGradient>
        <linearGradient id="truckGrad" x1="0" y1="0" x2="0" y2="1">
          <stop offset="0" stop-color="#2f8fd6"/>
          <stop offset="1" stop-color="#1b5f9e"/>
        </linearGradient>
      </defs>
      <polygon points="266,0 1133,0 1133,506 588,506" fill="url(#skyGrad)"/>
      <polygon points="588,0 984,0 724,506 588,506 428,256" fill="var(--deep-blue)"/>
      <rect x="475" y="118" width="555" height="320" rx="30" fill="url(#truckGrad)" opacity=".5"/>
    </svg>

    <div class="brand"><span class="brand-mark"></span><span class="brand-name">Rovilent</span></div>

    <div class="hero-phone">
      <svg width="18" height="18" viewBox="0 0 24 24" fill="none" stroke="#fff" stroke-width="1.6" stroke-linecap="round" stroke-linejoin="round"><path d="M22 16.9v3a2 2 0 0 1-2.2 2 19.8 19.8 0 0 1-8.6-3.1 19.5 19.5 0 0 1-6-6A19.8 19.8 0 0 1 2.1 4.2 2 2 0 0 1 4.1 2h3a2 2 0 0 1 2 1.7c.1 1 .4 1.9.7 2.8a2 2 0 0 1-.5 2.1L8 9.9a16 16 0 0 0 6 6l1.3-1.3a2 2 0 0 1 2.1-.4c.9.3 1.8.6 2.8.7a2 2 0 0 1 1.7 2z"/></svg>
      <span>+1 (555) 214-0387</span>
    </div>

    <a class="client-login">
      <svg width="11" height="12" viewBox="0 0 11 12" fill="none" stroke="#fff" stroke-width="1.3"><rect x="1" y="5" width="9" height="6.3" rx="1"/><path d="M3 5V3.5a2.5 2.5 0 0 1 5 0V5"/></svg>
      CLIENT LOG-IN
    </a>

    <h1 class="hero-copy">Will provide a<br>one stop solution for your<br><strong>Logistics Services</strong><br>needs.</h1>
    <a class="btn-outline">Learn more +</a>

    <div class="slider-dots"><span></span><span></span><span></span></div>
  </header>

  <svg class="section-bg" width="1133" height="506" viewBox="0 0 1133 506">
    <polygon points="0,0 400,0 662,506 0,506" fill="var(--grey-band)"/>
  </svg>

  <nav class="main-nav">
    <a style="left:446px">LOGISTIC SERVICES</a>
    <a style="left:588px">WAREHOUSE OPERATIONS</a>
    <a style="left:768px">ABOUT US</a>
    <a style="left:863px">TECHNOLOGY</a>
    <a style="left:970px">BLOG</a>
  </nav>

  <svg class="expertise-tag" width="270" height="102" viewBox="0 0 270 102">
    <polygon points="196,64 264,64 218,101" fill="#cfd0d2"/>
    <polygon points="0,0 232,0 264,64 32,64" fill="var(--brand-blue)"/>
  </svg>
  <div class="expertise-title">Expertise</div>

  <ul class="expertise-list">
    <li class="expertise-item" style="top:4px"><span class="expertise-num">01.</span><span class="expertise-label">Auto shipment to &amp; from USA via</span></li>
    <li class="expertise-rule" style="top:48px"></li>
    <li class="expertise-item" style="top:59px"><span class="expertise-num">02.</span><span class="expertise-label">Agricultural Product Handling</span></li>
    <li class="expertise-rule" style="top:100px"></li>
    <li class="expertise-item" style="top:114px"><span class="expertise-num">03.</span><span class="expertise-label" style="top:4px">Project Cargos</span></li>
    <li class="expertise-rule" style="top:148px"></li>
    <li class="expertise-item" style="top:158px"><span class="expertise-num">04.</span><span class="expertise-label" style="top:4px">Bulk Cargos</span></li>
  </ul>

  <svg class="quote-btn" width="266" height="66" viewBox="0 0 266 66">
    <polygon points="0,0 232,0 264,64 32,64" fill="var(--ink)"/>
  </svg>
  <div class="quote-label">Request A Quote
    <svg width="18" height="16" viewBox="0 0 18 16" fill="none" stroke="#fff" stroke-width="2.2" stroke-linecap="round" stroke-linejoin="round"><path d="M2 8h13M9 2l6 6-6 6"/></svg>
  </div>

  <section class="partners" aria-label="Partner carriers">
    <div class="partner" style="left:58px;width:80px;height:30px"></div>
    <div class="partner" style="left:234px;width:120px;height:30px"></div>
    <div class="partner" style="left:448px;width:48px;height:30px"></div>
    <div class="partner" style="left:588px;width:64px;height:30px"></div>
    <div class="partner" style="left:726px;width:84px;height:30px"></div>
    <div class="partner" style="left:898px;width:56px;height:30px"></div>
    <div class="partner" style="left:1057px;top:36px;width:38px;height:38px;border-radius:50%"></div>
  </section>

  <footer>
    <div class="footer-left">© 2017 ROVILENT.COM<br>Address:48 Harbor Line Drive Suite B, Linden Falls, NJ 07300</div>
    <div class="footer-right">Telephone:+1 (555) 214-0387<br>E-mail:support@rovilent.net</div>
  </footer>

</div>
</body>
</html>
```